business card for LWR pty ltd

We require a business card that stands out . I have included our company flyer and would like the services listed to be put on the card so when we Give out the cards to customers they have an idea of services we provide. need the winning design to be in editable photo shop format, editable iMac pages format or editable windows publisher format, so that I can enter in names, email addresses, phone numbers etc myself. I have included a pdf documents of info / items needed on the card to use as reference please.
Updates

need more submissions

Need extra days to review

Sick

Target Market(s)

new customers

Contact Information for Business Card

details are on attached business card requirements file

Requirements
Must have
• I have attached a list of must haves

```html
<!DOCTYPE html>
<html lang="en">
<head>
<meta charset="utf-8">
<title>LWR pty ltd – Business Card</title>
<link rel="stylesheet" href="https://fonts.googleapis.com/css2?family=Open+Sans:ital,wght@0,400;0,700;1,400&family=Orbitron:wght@500&display=swap">
<style>
  :root{
    --page:#eeeeee;
    --black:#050505;
    --mesh-light:#2a2a2a;
    --mesh-dark:#060606;
    --grey-top:#8e8e8e;
    --grey-bottom:#3c3c3c;
    --silver:#c9c9c9;
    --stripe:#bdbdbd;
    --brown-light:#8d7055;
    --brown-dark:#5f4a38;
    --amber:#f2b21c;
    --white:#ffffff;
    --banner-text:#5a4a2c;
    --photo-a:#7a7f86;
    --photo-b:#3f3a34;
  }
  *{box-sizing:border-box;margin:0;padding:0}
  html,body{width:1200px;height:1200px;overflow:hidden;background:var(--page)}
  body{position:relative;font-family:"Open Sans",Arial,sans-serif;color:var(--white)}

  .card{
    position:absolute;left:192px;width:750px;height:450px;
    transform-origin:0 0;transform:scale(1.0907);
    background:var(--black);overflow:hidden;
  }
  .card--front{top:74px}
  .card--back{top:631px}
  .card__shapes{position:absolute;inset:0;width:750px;height:450px}

  .mesh,.photo{position:absolute}
  .mesh{background:radial-gradient(ellipse at 45% 45%,var(--mesh-light),var(--mesh-dark) 75%)}
  .photo{background:linear-gradient(160deg,var(--photo-a),var(--photo-b));border-radius:6px}

  .wordmark{
    position:absolute;font-family:"Open Sans",Arial,sans-serif;font-weight:700;
    color:var(--silver);letter-spacing:4px;line-height:1;
  }

  /* front */
  .card--front .mesh{left:16px;top:62px;width:344px;height:262px}
  .card--front .wordmark{left:62px;top:140px;font-size:92px}
  .card--front .photo{left:14px;top:272px;width:446px;height:168px}

  .contact{position:absolute;right:34px;top:150px;text-align:right;font-size:17px;line-height:28px}
  .contact__company{font-weight:700}
  .contact__icons{position:absolute;left:721px;top:181px;width:20px;height:80px}

  .person{position:absolute;right:45px;top:368px;text-align:right}
  .person__name{font-size:28px;font-weight:700;line-height:34px}
  .person__role{font-size:17px;font-style:italic;color:var(--amber);line-height:22px}

  /* back */
  .banner{
    position:absolute;left:28px;top:34px;font-family:"Orbitron","Open Sans",sans-serif;
    font-weight:500;font-size:24px;letter-spacing:2px;color:var(--banner-text);
  }
  .card--back .mesh{left:0;top:72px;width:330px;height:210px}
  .card--back .wordmark{left:42px;top:118px;font-size:84px}
  .card--back .photo{left:30px;top:215px;width:385px;height:217px}

  .services{list-style:none;position:absolute;inset:0;font-size:15.5px}
  .services li{
    position:absolute;white-space:nowrap;line-height:20px;
    left:calc(365px + var(--i) * 16.2px);top:calc(76px + var(--i) * 21.7px);
  }
  .services li::before{content:"•";color:var(--amber);margin-right:6px}
  .services li.services__wrap{left:552px;top:314px}
  .services li.services__wrap::before{content:none}

  .web{position:absolute;left:446px;top:388px;display:flex;align-items:center;gap:9px;font-size:27px;font-weight:700}
</style>
</head>
<body>

<section class="card card--front" aria-label="Business card front">
  <svg class="card__shapes" viewBox="0 0 750 450" aria-hidden="true">
    <defs>
      <linearGradient id="greyPanelFront" x1="1" y1="0" x2="0.3" y2="1">
        <stop offset="0" stop-color="var(--grey-top)"/>
        <stop offset="1" stop-color="var(--grey-bottom)"/>
      </linearGradient>
      <linearGradient id="brownBandFront" x1="0" y1="0" x2="1" y2="0">
        <stop offset="0" stop-color="var(--brown-light)"/>
        <stop offset="1" stop-color="var(--brown-dark)"/>
      </linearGradient>
    </defs>
    <polygon points="536,30 750,30 750,356 330,356" fill="url(#greyPanelFront)"/>
    <polygon points="482,70 508,70 352,340 330,340" fill="var(--stripe)" opacity="0.8"/>
    <rect x="0" y="356" width="750" height="94" fill="url(#brownBandFront)"/>
    <rect x="455" y="353" width="295" height="3" fill="var(--amber)"/>
    <rect x="730" y="30" width="2" height="326" fill="var(--amber)"/>
  </svg>

  <div class="mesh" role="img" aria-label="Dark honeycomb metal mesh texture"></div>
  <div class="wordmark">LWR</div>
  <div class="photo" role="img" aria-label="Road train truck hauling water tanker trailers"></div>

  <div class="contact">
    <p class="contact__company">LWR pty ltd</p>
    <p>000 444 000</p>
    <p>email@lwrservices.com.au</p>
    <p>Depot: Lot 444</p>
    <p>example address Australia</p>
  </div>
  <svg class="contact__icons" viewBox="0 0 20 80" aria-hidden="true">
    <circle cx="10" cy="10" r="9" fill="var(--white)"/>
    <path d="M6.5 5.5l2 0 1 2.5-1.3 1a6 6 0 0 0 3 3l1-1.3 2.5 1v2a1 1 0 0 1-1 1A8.5 8.5 0 0 1 5.5 6.5a1 1 0 0 1 1-1z" fill="var(--grey-bottom)"/>
    <circle cx="10" cy="38" r="9" fill="var(--white)"/>
    <rect x="5" y="34.5" width="10" height="7" rx="1" fill="none" stroke="var(--grey-bottom)" stroke-width="1.4"/>
    <path d="M5.5 35l4.5 3.5 4.5-3.5" fill="none" stroke="var(--grey-bottom)" stroke-width="1.3"/>
    <circle cx="10" cy="66" r="9" fill="var(--white)"/>
    <path d="M10 60.5a3.6 3.6 0 0 0-3.6 3.6c0 2.7 3.6 6.4 3.6 6.4s3.6-3.7 3.6-6.4a3.6 3.6 0 0 0-3.6-3.6z" fill="var(--amber)"/>
    <circle cx="10" cy="64" r="1.3" fill="var(--white)"/>
  </svg>

  <div class="person">
    <p class="person__name">Daniel Harlow</p>
    <p class="person__role">Director</p>
  </div>
</section>

<section class="card card--back" aria-label="Business card back">
  <svg class="card__shapes" viewBox="0 0 750 450" aria-hidden="true">
    <defs>
      <linearGradient id="greyPanelBack" x1="1" y1="0" x2="0.3" y2="1">
        <stop offset="0" stop-color="var(--grey-top)"/>
        <stop offset="1" stop-color="var(--grey-bottom)"/>
      </linearGradient>
      <linearGradient id="brownBandBack" x1="0" y1="0" x2="1" y2="0">
        <stop offset="0" stop-color="var(--brown-light)"/>
        <stop offset="1" stop-color="var(--brown-dark)"/>
      </linearGradient>
    </defs>
    <polygon points="282,0 750,0 750,356 532,356" fill="url(#greyPanelBack)"/>
    <polygon points="262,0 266,0 514,356 510,356" fill="var(--amber)"/>
    <polygon points="0,27 318,27 345,72 0,72" fill="var(--amber)"/>
    <rect x="0" y="356" width="750" height="94" fill="url(#brownBandBack)"/>
    <rect x="0" y="353" width="750" height="3" fill="var(--amber)"/>
  </svg>

  <p class="banner">OUR SERVICES</p>
  <div class="mesh" role="img" aria-label="Dark honeycomb metal mesh texture"></div>
  <div class="wordmark">LWR</div>
  <div class="photo" role="img" aria-label="Two prime mover trucks with bull bars, front view"></div>

  <ul class="services">
    <li style="--i:0">Over size loads / Hot Shot Loads</li>
    <li style="--i:1">Heavy Vehicle Recovery services</li>
    <li style="--i:2">Potable Water Deliveries</li>
    <li style="--i:3">Road Building / Maintenance</li>
    <li style="--i:4">Earthworks</li>
    <li style="--i:5">Sand &amp; Metal Supply &amp; Cartage</li>
    <li style="--i:6">Road Train Tippers</li>
    <li style="--i:7">Road Train Tankers</li>
    <li style="--i:8">Road Train Flat Tops</li>
    <li style="--i:9">Drop Deck Trailers</li>
    <li style="--i:10">Mine site accredited</li>
    <li class="services__wrap">equipment &amp; Operators</li>
  </ul>

  <p class="web">
    <svg width="20" height="20" viewBox="0 0 20 20" aria-hidden="true">
      <circle cx="10" cy="10" r="8.5" fill="none" stroke="var(--amber)" stroke-width="2"/>
      <ellipse cx="10" cy="10" rx="3.5" ry="8.5" fill="none" stroke="var(--amber)" stroke-width="1.6"/>
      <path d="M1.5 10h17M3 5.5h14M3 14.5h14" stroke="var(--amber)" stroke-width="1.4"/>
    </svg>
    www.website.com
  </p>
</section>

</body>
</html>
```